Business Card for Managing Partner Investment Fund

To create a business card template for an investment fund manager. Business card should be more professional in nature, not too colorful, more upscale, and created using the attached logos and fund name files. I would prefer a black or gray color scheme, but am open to the use of color as well. I would prefer a double sided business card, but open to single sided business card designs as well. The business card should include: name, title, and contact information, as well as logo and company name. I would prefer a more stream-lined, simple business card design.
Updates
Address: 4136 NE 19th Ter. Ocala, FL 34470
Email: travis48@quillnet-mail.com
Phone: 561-374-9186
Title: managing partner
Name: Travis Whitlow
Fund Name: Emberfall Capital
Logos can be found in files attached to the brief
Target Market(s)
potential investors, other fund managers
Industry/Entity Type
Finance
Contact Information for Business Card
Name on card: Travis Whitlow
Title: Managing Partner
Font styles to use
Colors
Designer to choose colors to be used in the design.
Requirements
Must have
- Phone number
- email address
- physical address
- title
- name
- logo
- Fund name
Nice to have
- simple layout
Should not have
- too many colors, busy fonts,

```html
<!DOCTYPE html>
<html lang="en">
<head>
<meta charset="utf-8">
<title>Emberfall Capital – Business Card</title>
<link rel="stylesheet" href="https://fonts.googleapis.com/css2?family=Roboto:wght@400;500&family=Roboto+Condensed:wght@500&display=swap">
<style>
  :root {
    --stage: #2b2b2b;
    --card-white: #f0f0f0;
    --card-grey: #616161;
    --ink-dark: #555555;
    --ink-mid: #6a6a6a;
    --ink-light: #8a8a8a;
    --accent-bar: #6b6b6b;
    --rule: #9a9a9a;
    --snow-top: #d9d9d9;
    --snow-bottom: #ffffff;
    --white: #ffffff;
  }
  * { margin: 0; padding: 0; box-sizing: border-box; }
  html, body { width: 1200px; height: 960px; overflow: hidden; }
  body {
    background: var(--stage);
    font-family: "Roboto", Arial, sans-serif;
    position: relative;
  }
  .card {
    position: absolute;
    width: 600px;
    height: 343px;
    overflow: hidden;
  }
  /* Front */
  .card--front { left: 314px; top: 113px; background: var(--card-white); }
  .brand-name {
    position: absolute;
    right: 40px;
    top: 88px;
    text-align: right;
    font-family: "Roboto", Arial, sans-serif;
    font-weight: 500;
    font-size: 24px;
    line-height: 30px;
    letter-spacing: 2px;
    color: var(--ink-mid);
    text-transform: uppercase;
  }
  .accent-bar {
    position: absolute;
    left: 0; top: 192px;
    width: 11px; height: 45px;
    background: var(--accent-bar);
  }
  .holder-name {
    position: absolute;
    left: 48px; top: 193px;
    font-family: "Roboto Condensed", "Arial Narrow", sans-serif;
    font-weight: 500;
    font-size: 22px;
    color: var(--ink-dark);
    text-transform: uppercase;
  }
  .holder-title {
    position: absolute;
    left: 48px; top: 220px;
    font-size: 15px;
    letter-spacing: 0.3px;
    color: var(--ink-light);
    text-transform: uppercase;
  }
  .contact-list {
    position: absolute;
    left: 48px; top: 248px;
    list-style: none;
    font-size: 14px;
    line-height: 19px;
    color: var(--ink-dark);
  }
  .contact-list li { display: flex; align-items: center; gap: 8px; }
  .contact-list svg { width: 13px; height: 13px; fill: var(--ink-dark); flex: none; }
  .contact-divider {
    position: absolute;
    left: 242px; top: 268px;
    width: 1px; height: 34px;
    background: var(--rule);
  }
  .address {
    position: absolute;
    left: 262px; top: 267px;
    font-size: 14px;
    line-height: 19px;
    font-style: normal;
    color: var(--ink-dark);
  }
  /* Back */
  .card--back { left: 311px; top: 472px; background: var(--card-grey); }
  .back-brand {
    position: absolute;
    left: 44px; top: 32px;
    font-weight: 500;
    font-size: 26px;
    line-height: 30px;
    letter-spacing: 2px;
    color: var(--white);
    text-transform: uppercase;
  }
  .back-web {
    position: absolute;
    left: 44px; top: 95px;
    font-size: 14px;
    letter-spacing: 3.2px;
    color: var(--white);
  }
  .back-scenery {
    position: absolute;
    left: 0; right: 0; bottom: 0;
    height: 200px;
    background: linear-gradient(180deg, var(--snow-top), var(--snow-bottom));
  }
</style>
</head>
<body>
  <section class="card card--front" aria-label="Business card front">
    <div class="brand-name">Emberfall<br>Capital</div>
    <div class="accent-bar"></div>
    <h1 class="holder-name">Travis Whitlow</h1>
    <p class="holder-title">Managing Partner</p>
    <ul class="contact-list">
      <li>
        <svg viewBox="0 0 24 24" aria-hidden="true"><path d="M6.6 10.8a15.1 15.1 0 0 0 6.6 6.6l2.2-2.2a1 1 0 0 1 1-.25 11.4 11.4 0 0 0 3.6.57 1 1 0 0 1 1 1V20a1 1 0 0 1-1 1A17 17 0 0 1 3 4a1 1 0 0 1 1-1h3.5a1 1 0 0 1 1 1c0 1.25.2 2.45.57 3.57a1 1 0 0 1-.25 1z"/></svg>
        561-374-9186
      </li>
      <li>
        <svg viewBox="0 0 24 24" aria-hidden="true"><path d="M2 5h20v14H2z M2 5l10 8 10-8" /></svg>
        travis48@quillnet-mail.com
      </li>
      <li>
        <svg viewBox="0 0 24 24" aria-hidden="true"><circle cx="12" cy="12" r="10"/></svg>
        www.emberfall-cap.com
      </li>
    </ul>
    <div class="contact-divider"></div>
    <address class="address">4136 NE 19th Ter.<br>Ocala, FL 34470</address>
  </section>

  <section class="card card--back" aria-label="Business card back">
    <div class="back-brand">Emberfall<br>Capital</div>
    <div class="back-web">www.emberfall-cap.com</div>
    <div class="back-scenery" role="img" aria-label="Large snow-capped mountain range illustration in white and grey"></div>
  </section>
</body>
</html>
```